Hong Kong residential leasing and sales company needs a website design

Hong Kong has many competitive real estate agents. The majority of us have the same listings so, besides the team and experience, a website is what makes us stand out. A first impression. We need our website to be user friendly, informative and to have a wow factor. Most sites are generic so whilst we are close to accepting that maybe that's the only formula which works....we would like to see if we're missing something! Our clients are a mix of International users of all ages but probably ultimately 35+.. We have a logo (attached) which we would like to keep - designed by brushforum. Flexible with colours except red.
examples of our competitors are:
http://www.marlowvesthomes.example
http://www.tuvix.example/home
http://www.premierdwellingsgr.example
http://www.nestora-estates.example
http://www.fieldmark-ardley.example
We were thinking of having the following in a menu bar with drop downs for most...some more than others. Home / For Sale / For Rent / Property 101 / About us / Contact Us ..
Look forward to seeing your ideas. Thanks in advance.

```html
<!DOCTYPE html>
<html lang="en">
<head>
<meta charset="utf-8">
<title>Lumen Property</title>
<link href="https://fonts.googleapis.com/css2?family=Roboto:wght@300;400;500;700&display=swap" rel="stylesheet">
<style>
:root{
  --purple:#5a3275;
  --accent:#9b3fc7;
  --dark:#2f3438;
  --text:#444;
  --muted:#8a8a8a;
  --line:#e2e2e2;
  --panel:#f5f5f5;
  --footer-text:#d9cbe4;
}
*{box-sizing:border-box;margin:0;padding:0}
html,body{width:921px;height:1200px;overflow:hidden}
body{position:relative;font-family:"Roboto",sans-serif;color:var(--text);background:var(--purple);font-size:8px}
.abs{position:absolute}
.header{left:0;top:0;width:921px;height:85px;background:#fff}
.topbar{left:156px;top:0;width:610px;height:26px;border-bottom:1px solid var(--line)}
.topbar .email{left:0;top:9px;font-size:7px;color:var(--muted)}
.social{right:0;top:0;display:flex;height:25px}
.social span{width:26px;height:25px;border-left:1px solid var(--line);display:flex;align-items:center;justify-content:center}
.social span i{width:6px;height:6px;border-radius:50%;background:#8a8f94}
.brand{left:158px;top:40px;display:flex;align-items:center;gap:5px;font-size:12px;font-weight:500;color:var(--purple);letter-spacing:1px}
.brand i{width:12px;height:12px;background:var(--purple)}
.nav{left:271px;top:60px;display:flex;font-size:8px;color:#555}
.nav a{padding:9px 9px 0;height:24px;text-decoration:none;color:inherit;margin-right:6px}
.nav a.active{background:var(--accent);color:#fff}
.call{right:155px;top:52px;text-align:right}
.call small{font-size:6.5px;color:var(--muted)}
.call b{display:flex;align-items:center;gap:4px;font-size:13px;color:var(--accent);font-weight:500;margin-top:2px}
.hero{left:0;top:85px;width:921px;height:329px;background:linear-gradient(172deg,#b9b1a8 0%,#e9e6e1 22%,#f4f3f0 40%,#d6d0c6 58%,#8f7b66 74%,#5f7a3c 88%,#3f5a28 100%)}
.caption{left:156px;top:178px;width:254px;height:76px;background:rgba(255,255,255,.82);padding:11px 12px}
.caption h2{font-size:12.5px;font-weight:500;color:#222}
.caption p{font-size:6.5px;color:#666;line-height:12px;margin-top:4px}
.caption .price{font-size:9px;color:#333;margin-top:2px}
.btn{background:var(--accent);color:#fff;font-size:6.5px;display:flex;align-items:center;justify-content:center}
.know{left:156px;top:256px;width:49px;height:16px}
.arrow{width:26px;height:26px;border-radius:50%;border:2px solid #fff;display:flex;align-items:center;justify-content:center}
.find{left:156px;top:386px;width:144px;height:28px;background:rgba(47,52,56,.92);color:#fff;display:flex;align-items:center;font-size:10.5px;font-weight:500}
.find .icon{width:30px;height:28px;display:flex;align-items:center;justify-content:center;background:#24282b;margin-right:10px}
.panel{left:156px;top:414px;width:610px;height:472px;background:#fff}
.field{position:absolute;font-size:7px;color:#444}
.field .sel{margin-top:6px;height:18px;border:1px solid #d6d6d6;font-size:7px;color:#888;padding:5px 6px;position:relative}
.field .sel:after{content:"";position:absolute;right:0;top:0;width:15px;height:16px;border-left:1px solid #d6d6d6}
.search{left:543px;top:73px;width:49px;height:17px}
.featured{left:0;top:108px;width:610px;height:280px;background:var(--panel)}
.featured h3{position:absolute;left:28px;top:26px;font-size:12.5px;font-weight:500;color:#222}
.featured .lead{position:absolute;left:28px;top:48px;font-size:6.5px;color:#777}
.card{position:absolute;top:80px;width:127px}
.card .img{height:84px}
.card h4{font-size:7px;font-weight:400;color:#333;margin-top:11px;white-space:nowrap}
.card p{font-size:6.3px;color:#888;line-height:11px;margin-top:3px}
.card .tag{display:inline-block;background:var(--dark);color:#fff;font-size:6.3px;padding:2px 5px;margin-top:5px}
.side{position:absolute;width:13px;height:20px;display:flex;align-items:center;justify-content:center}
.partners-title{left:260px;top:390px;width:87px;height:19px;background:var(--dark);color:#fff;font-size:6.8px;font-weight:500;display:flex;align-items:center;justify-content:center}
.badge{position:absolute;top:428px;height:16px;background:#cfcfcf;border-radius:3px}
.footer-col{position:absolute;top:910px;color:var(--footer-text);font-size:6.5px;line-height:11px}
.footer-col h5{font-size:9.5px;font-weight:400;color:#e7ddef;margin-bottom:14px}
.footer-col ul{list-style:none}
.footer-col li{margin-bottom:5px}
.footer-col li:before{content:"›";margin-right:4px}
.rule{left:156px;top:1038px;width:610px;height:1px;background:rgba(255,255,255,.25)}
.legal{top:1053px;font-size:6.5px;color:var(--footer-text)}
.skyline{left:0;top:1075px;width:921px;height:125px;background:linear-gradient(180deg,rgba(140,108,168,0) 0%,#7d5e98 40%,#9a80b3 100%)}
</style>
</head>
<body>
<div class="abs header"></div>
<div class="abs topbar">
  <div class="abs email">Email us at : info@lumenproperty.example</div>
  <div class="abs social"><span><i></i></span><span><i></i></span><span><i></i></span><span><i></i></span><span><i></i></span><span style="border-right:1px solid var(--line)"><i></i></span></div>
</div>
<div class="abs brand"><i></i>LUMEN PROPERTY</div>
<nav class="abs nav"><a class="active">Home</a><a>For Sale</a><a>For Rent</a><a>Property 101</a><a>About us</a><a>Contact Us</a></nav>
<div class="abs call"><small>For inquiries, please call us:</small><b><svg width="10" height="10" viewBox="0 0 10 10"><path d="M2 1l2 2-1 1.2c.6 1.2 1.6 2.2 2.8 2.8L7 6l2 2-1.3 1.3C4.5 9 1 5.5.7 2.3z" fill="#888"/></svg>1-800-555-0199</b></div>

<div class="abs hero" role="img" aria-label="Bright open-plan loft interior with bedroom, staircase, kitchen and indoor plants"></div>
<div class="abs arrow" style="left:28px;top:212px;border-color:#444"><svg width="8" height="8"><path d="M5.5 1L2.5 4l3 3" stroke="#444" stroke-width="1.5" fill="none"/></svg></div>
<div class="abs arrow" style="left:839px;top:212px"><svg width="8" height="8"><path d="M2.5 1l3 3-3 3" stroke="#fff" stroke-width="1.5" fill="none"/></svg></div>
<div class="abs caption">
  <h2>18 Harbour View Rd, Kowloon</h2>
  <p>Lorem ipsum dolor sit amet, consectetu adipiscing elit, sed diam nonummy nibh euismod tincidunt ut laoreet dolore</p>
  <div class="price">$380,000</div>
</div>
<div class="abs btn know">Know More</div>
<div class="abs find"><span class="icon"><svg width="10" height="10"><circle cx="4" cy="4" r="3" stroke="#fff" stroke-width="1.4" fill="none"/><path d="M6.3 6.3L9 9" stroke="#fff" stroke-width="1.5"/></svg></span>Find your Home</div>

<div class="abs panel">
  <div class="field" style="left:16px;top:14px;width:186px">Location<div class="sel">Select</div></div>
  <div class="field" style="left:215px;top:14px;width:182px">Status<div class="sel">Select</div></div>
  <div class="field" style="left:410px;top:14px;width:182px">Bedrooms<div class="sel">Select</div></div>
  <div class="field" style="left:16px;top:59px;width:119px">Bathrooms<div class="sel">Select</div></div>
  <div class="field" style="left:147px;top:59px;width:119px">Minimum Price<div class="sel">Select</div></div>
  <div class="field" style="left:278px;top:59px;width:119px">Maximum Price<div class="sel">Select</div></div>
  <div class="field" style="left:410px;top:59px;width:119px">Property Type<div class="sel">Select</div></div>
  <div class="abs btn search">Search</div>

  <div class="abs featured">
    <h3>Featured Properties</h3>
    <div class="lead">Look at our Latest listed properties and check out the facilities on them, We have already sold more than 50,000 Homes.</div>
    <div class="side" style="left:0;top:108px;background:#e4e4e4"><svg width="4" height="5"><path d="M3 0v5L0 2.5z" fill="#555"/></svg></div>
    <div class="side" style="left:597px;top:108px;background:var(--dark)"><svg width="4" height="5"><path d="M1 0v5l3-2.5z" fill="#fff"/></svg></div>
    <div class="card" style="left:27px"><div class="img" role="img" aria-label="Modern lounge with white chairs and orange cushions" style="background:linear-gradient(160deg,#5f6b63 0%,#9aa8a6 35%,#e2e6e4 60%,#c7cbc9 78%,#d98a2b 100%)"></div><h4>42 Peak Crest Rd, Mid-Levels</h4><p>Lorem ipsum dolor sit amet, consectetu adipiscing elit, sed diam...</p><span class="tag">$740000</span></div>
    <div class="card" style="left:169px"><div class="img" role="img" aria-label="Contemporary house exterior with lawn and trees" style="background:linear-gradient(180deg,#4d6e22 0%,#9fb3a8 30%,#dfe2df 55%,#8a8f88 70%,#5f8f2c 85%,#3f6a1c 100%)"></div><h4>18 Harbour View Rd, Kowloon</h4><p>Lorem ipsum dolor sit amet, consectetu adipiscing elit, sed diam...</p><span class="tag">$820000</span></div>
    <div class="card" style="left:311px"><div class="img" role="img" aria-label="White living room with sofa and blinds" style="background:linear-gradient(180deg,#7d6f5b 0%,#b9ad98 35%,#e8e6e1 62%,#f4f4f2 80%,#9a9892 100%)"></div><h4>9 Lantern Lane, Sai Kung</h4><p>Lorem ipsum dolor sit amet, consectetu adipiscing elit, sed diam...</p><span class="tag">$570000</span></div>
    <div class="card" style="left:453px"><div class="img" role="img" aria-label="Living room with yellow armchair and shelving" style="background:linear-gradient(135deg,#f1ede6 0%,#d8d3c9 40%,#e0b22a 65%,#c79410 80%,#5a4a36 100%)"></div><h4>27 Bayside Terrace, Stanley</h4><p>Lorem ipsum dolor sit amet, consectetu adipiscing elit, sed diam...</p><span class="tag">$930000</span></div>
  </div>

  <div class="abs" style="left:0;top:388px;width:610px;height:1px;background:var(--line)"></div>
  <div class="abs partners-title">Featured Partners</div>
  <div class="side" style="left:0;top:426px;background:#e4e4e4"><svg width="4" height="5"><path d="M3 0v5L0 2.5z" fill="#555"/></svg></div>
  <div class="side" style="left:597px;top:426px;background:#e4e4e4"><svg width="4" height="5"><path d="M1 0v5l3-2.5z" fill="#555"/></svg></div>
  <div class="badge" style="left:35px;width:72px"></div>
  <div class="badge" style="left:133px;width:52px"></div>
  <div class="badge" style="left:211px;width:72px"></div>
  <div class="badge" style="left:318px;width:46px"></div>
  <div class="badge" style="left:399px;width:64px"></div>
  <div class="badge" style="left:495px;width:73px"></div>
</div>

<div class="footer-col" style="left:156px;width:145px"><h5>About Lumen Property</h5><p>Aquam est tortor, sagittis in fringilla in, pellent esque nec erat. Aenean semper, neque non faucibus.</p><p style="margin-top:11px">Malesuada, dui felis tempor felis, vel varius ante diam ut mauris.</p></div>
<div class="footer-col" style="left:312px"><h5>Quick Links</h5><ul><li>Single Family</li><li>New Construction</li><li>On Rent</li><li>On Sale</li></ul></div>
<div class="footer-col" style="left:389px;top:935px"><ul><li>Single Family</li><li>New Construction</li><li>On Rent</li><li>On Sale</li></ul></div>
<div class="footer-col" style="left:468px;width:145px"><h5>Quick Links</h5><ul><li>Aquam est tortor, sagittis in fringilla in, pell esque nec erat.</li><li style="margin-top:11px">Aenean semper, neque non faucibus.</li><li style="margin-top:11px">Malesuada, dui felis tempor felis, vel varius</li></ul></div>
<div class="footer-col" style="left:625px;width:145px"><h5>Contact Info</h5><p>27 Bayside Terrace, Stanley.<br>Lantern Lane, HK</p><p style="margin-top:11px">Phone : 123-456-0000</p><p style="margin-top:11px">Email : info@lumenproperty.example</p></div>
<div class="abs rule"></div>
<div class="abs legal" style="left:156px">© 2014 All Rights Reserved by Lumen Property</div>
<div class="abs legal" style="right:158px">Site Map &nbsp;&nbsp; / &nbsp;&nbsp; Privacy Policy</div>
<div class="abs skyline" role="img" aria-label="Silhouetted city skyline along the bottom edge"></div>
</body>
</html>
```